Inspiration Poster

Inspirational Poster that has a Kamran Dulo like abstract look (http://www.vexalo.com/images/search?q=kamran+dulo&FORM=HDRSC2) with the text:

"we walk not in order to arrive at the promise land but because walking itself is a revolution"
-Peter Ambrick

```html
<!DOCTYPE html>
<html lang="en">
<head>
<meta charset="utf-8">
<title>Inspiration Poster</title>
<link rel="stylesheet" href="https://fonts.googleapis.com/css2?family=Anton&display=swap">
<style>
  :root {
    --frame: #0b0a09;
    --stone-light: #b3a594;
    --stone-mid: #8e7f6f;
    --stone-dark: #5a4c40;
    --ink: #2a231e;
    --byline: #ffffff;
  }
  html, body {
    margin: 0;
    padding: 0;
    width: 1200px;
    height: 834px;
    overflow: hidden;
    background: var(--frame);
  }
  .poster {
    position: relative;
    width: 1200px;
    height: 834px;
    background: var(--frame);
  }
  .poster__texture {
    position: absolute;
    left: 30px;
    top: 32px;
    right: 34px;
    bottom: 46px;
    background:
      radial-gradient(ellipse at 45% 40%, var(--stone-light) 0%, var(--stone-mid) 55%, var(--stone-dark) 100%);
    box-shadow: inset 0 0 28px 10px var(--frame);
  }
  .poster__quote {
    position: absolute;
    inset: 0;
    width: 1200px;
    height: 834px;
  }
  .quote__line {
    font-family: "Anton", sans-serif;
    font-size: 70px;
    fill: var(--ink);
    text-transform: uppercase;
  }
  .quote__byline {
    font-family: "Anton", sans-serif;
    font-size: 34px;
    fill: var(--byline);
    text-transform: uppercase;
  }
</style>
</head>
<body>
  <main class="poster">
    <div class="poster__texture" role="img" aria-label="Weathered, cracked sepia stone surface texture"></div>
    <svg class="poster__quote" viewBox="0 0 1200 834" xmlns="http://www.w3.org/2000/svg">
      <text class="quote__line" x="112" y="524" textLength="990" lengthAdjust="spacingAndGlyphs" transform="rotate(-15.9 112 524)">We walk not in order to arrive at</text>
      <text class="quote__line" x="180" y="596" textLength="896" lengthAdjust="spacingAndGlyphs" transform="rotate(-15.9 180 596)">The promise land but because</text>
      <text class="quote__line" x="200" y="672" textLength="900" lengthAdjust="spacingAndGlyphs" transform="rotate(-15.5 200 672)">Walking itself is a revolution</text>
      <text class="quote__byline" x="868" y="740" textLength="262" lengthAdjust="spacingAndGlyphs" transform="rotate(-18.5 868 740)">-Peter Ambrick</text>
    </svg>
  </main>
</body>
</html>
```